New Business Card Design Project

I would like my card design to look exactly like the logo, design, layout, and print of the current attached file. The only change I would like made would be for the print to say THE KMW GROUP instead of THE HALLORAN GROUP. Basically, just replace his group name with my group name. I would also like the backgroud to be the same texture and color as the attached file. I love the dark blue lettering and house logo on the card.

I am completely open to the rest of the card design. I just want something clean and simple. Only basic contact info required on the card. Maybe just name: Kyle M Warrick and cell # 555.914.2087 and email kyle@orchidhomesagent.com

```html
<!DOCTYPE html>
<html lang="en">
<head>
<meta charset="utf-8">
<title>The KMW Group – Business Card</title>
<link rel="stylesheet" href="https://fonts.googleapis.com/css2?family=Roboto:wght@400;700&display=swap">
<style>
  :root {
    --backdrop: #2c2c2e;
    --paper: #f2f2f0;
    --paper-shade: #e6e6e3;
    --navy: #15123a;
    --ink-grey: #7a7a80;
    --card-w: 620px;
    --card-h: 354px;
  }
  * { box-sizing: border-box; margin: 0; padding: 0; }
  html, body {
    width: 1200px;
    height: 886px;
    overflow: hidden;
    background: var(--backdrop);
  }
  .sheet {
    width: 1200px;
    height: 886px;
    display: flex;
    flex-direction: column;
    align-items: center;
    justify-content: center;
    gap: 50px;
  }
  .card {
    position: relative;
    width: var(--card-w);
    height: var(--card-h);
    background: linear-gradient(135deg, var(--paper) 0%, var(--paper-shade) 100%);
    box-shadow: 0 10px 24px rgba(0,0,0,0.35);
    overflow: hidden;
  }

  /* Front */
  .card--front .brand {
    position: absolute;
    left: 50%;
    top: 50%;
    transform: translate(-50%, -50%);
    display: flex;
    align-items: center;
    gap: 16px;
    white-space: nowrap;
  }
  .brand__square {
    width: 28px;
    height: 28px;
    background: var(--navy);
    flex: none;
  }
  .brand__name {
    font-family: "Roboto", sans-serif;
    font-weight: 700;
    color: var(--navy);
    font-size: 26px;
    line-height: 1;
  }

  /* Back */
  .card--back .block {
    position: absolute;
    left: 62px;
    bottom: 0;
    width: 250px;
    height: 250px;
    background: var(--navy);
  }
  .card--back .wordmark {
    position: absolute;
    right: 28px;
    top: 40px;
    font-family: "Roboto", sans-serif;
    font-weight: 700;
    color: var(--navy);
    font-size: 24px;
    line-height: 1;
    white-space: nowrap;
  }
  .contact {
    position: absolute;
    right: 28px;
    top: 170px;
    font-family: "Roboto", sans-serif;
    text-align: right;
    color: var(--ink-grey);
  }
  .contact__name {
    font-weight: 700;
    font-size: 16px;
    color: var(--navy);
    letter-spacing: 0.02em;
    margin-right: 22px;
  }
  .contact__title {
    font-size: 12px;
    margin: 2px 22px 10px 0;
    letter-spacing: 0.03em;
  }
  .contact__line {
    display: flex;
    justify-content: flex-end;
    align-items: center;
    gap: 8px;
    font-size: 13px;
    line-height: 20px;
  }
  .contact__icon {
    width: 13px;
    height: 13px;
    fill: var(--navy);
    flex: none;
  }
</style>
</head>
<body>
<main class="sheet">

  <section class="card card--front" aria-label="Business card front">
    <div class="brand">
      <span class="brand__square"></span>
      <p class="brand__name">THE KMW GROUP</p>
    </div>
  </section>

  <section class="card card--back" aria-label="Business card back">
    <span class="block"></span>
    <p class="wordmark">THE KMW GROUP</p>

    <div class="contact">
      <p class="contact__name">KYLE M WARRICK</p>
      <p class="contact__title">CEO/FOUNDER</p>

      <p class="contact__line">555.914.2087
        <svg class="contact__icon" viewBox="0 0 14 14" aria-hidden="true">
          <rect x="3" y="0.5" width="8" height="13" rx="1.5"/>
          <rect x="4.3" y="2" width="5.4" height="8.5" fill="#f2f2f0"/>
        </svg>
      </p>
      <p class="contact__line">kyle@orchidhomesagent.com
        <svg class="contact__icon" viewBox="0 0 14 14" aria-hidden="true">
          <rect x="0.5" y="2.5" width="13" height="9" rx="1"/>
          <path d="M1 3.2 L7 8 L13 3.2" stroke="#f2f2f0" stroke-width="1.1" fill="none"/>
        </svg>
      </p>
      <p class="contact__line">www.orchidhomesagent.com
        <svg class="contact__icon" viewBox="0 0 14 14" aria-hidden="true">
          <circle cx="7" cy="7" r="6.5"/>
          <ellipse cx="7" cy="7" rx="2.6" ry="6" stroke="#f2f2f0" stroke-width="1" fill="none"/>
          <path d="M1 7 H13" stroke="#f2f2f0" stroke-width="1"/>
        </svg>
      </p>
    </div>
  </section>

</main>
</body>
</html>
```